Real Estate agent needs flyer/folder to contain bio and overview of services

I'm including files of the layout of the small folder. The folder is 6 1/2 across and 9 1/2 inches long. It will have a front & back cover and then writing on the 2 inside pages.

I am sending a few files to incorporate into the flyer, 1 new logo to use and 2 files which are coloring ideas.

```html
<!DOCTYPE html>
<html lang="en">
<head>
<meta charset="utf-8">
<title>Folder – Left Hand Page Inside</title>
<link rel="stylesheet" href="https://fonts.googleapis.com/css2?family=Arimo:ital,wght@0,400;1,400&family=Kaushan+Script&family=Source+Sans+3:wght@400&display=swap">
<style>
  :root {
    --cream: #f3e3b3;
    --navy: #0c4a94;
    --white: #ffffff;
    --red: #e10600;
    --ink: #111111;
    --photo-light: #e9dcc4;
    --photo-dark: #2a2623;
  }
  * { margin: 0; padding: 0; box-sizing: border-box; }
  html, body { width: 1200px; height: 1200px; overflow: hidden; background: var(--cream); }
  .canvas { position: relative; width: 1200px; height: 1200px; background: var(--cream); overflow: hidden; }
  .backdrop { position: absolute; inset: 0; }
  .page-label {
    position: absolute; left: 1019px; top: 40px;
    font-family: "Source Sans 3", sans-serif; font-size: 18px; line-height: 24px;
    color: var(--ink); letter-spacing: 0.2px;
  }
  .content-panel { position: absolute; left: 457px; top: 120px; width: 478px; height: 922px; background: var(--white); }
  .portrait-shadow { position: absolute; left: 312px; top: 222px; width: 178px; height: 212px; background: var(--red); }
  .portrait {
    position: absolute; left: 299px; top: 203px; width: 179px; height: 215px;
    background: var(--white); border: 1px solid var(--ink); padding: 8px;
  }
  .portrait-fill {
    width: 100%; height: 100%;
    background: linear-gradient(180deg, var(--photo-light) 0%, #d9c49c 45%, var(--photo-dark) 100%);
  }
  .heading {
    position: absolute; left: 512px;
    font-family: "Kaushan Script", cursive; font-size: 29px; line-height: 36px;
    color: var(--ink); white-space: nowrap;
  }
  .rule { position: absolute; left: 512px; height: 3px; background: var(--red); }
  .copy {
    position: absolute; left: 512px; width: 402px;
    font-family: Arimo, sans-serif; font-size: 14.4px; line-height: 20px;
    color: var(--ink); text-align: justify;
  }
  .tagline { font-style: italic; }
</style>
</head>
<body>
<div class="canvas">
  <svg class="backdrop" width="1200" height="1200" viewBox="0 0 1200 1200" aria-hidden="true">
    <path d="M312 34 L972 34 L972 1174 L342 1174 Q65 596 312 34 Z" fill="var(--navy)" stroke="#000" stroke-width="1"/>
  </svg>

  <div class="page-label">LEFT HAND PAGE<br>INSIDE</div>

  <div class="content-panel"></div>

  <div class="portrait-shadow"></div>
  <div class="portrait">
    <div class="portrait-fill" role="img" aria-label="Portrait photo of the agent in a dark blazer"></div>
  </div>

  <h2 class="heading" style="top:156px;">Let me introduce myself</h2>
  <div class="rule" style="top:198px; width:262px;"></div>

  <p class="copy" style="top:216px;">I’m originally from Chicago, but I’m a full-fledged California girl now. I’ve lived and worked in Orange County since 1996. I always say where we live is the next best thing to living on a tropical island. I’ve traveled to many and I’m always happy to come back to my Laguna Niguel home.</p>

  <p class="copy" style="top:336px;">My passion for this area is why I’m in Real Estate. I consider myself incredibly fortunate to sell homes and help people purchase homes in an area that I love with all my heart.</p>

  <p class="copy" style="top:416px;">This passion also carries over in representing my clients with the highest degree of professionalism, enthusiasm and care. My business is built on exceptional customer service and I’m grateful my clients are mostly repeat and referrals.</p>

  <h2 class="heading" style="top:532px;">My Core Tenet</h2>
  <div class="rule" style="top:573px; width:166px;"></div>

  <p class="copy tagline" style="top:588px;">It’s All About YOU!</p>
  <p class="copy" style="top:608px;">My #1 priority is understanding YOUR needs and YOUR objectives. This understanding, along with working diligently on your behalf, means we accomplish your goal whether you’re purchasing your 1st home or selling a home you’ve loved so you can move on to the next chapter of your life</p>

  <h2 class="heading" style="top:738px;">Real Estate Services &amp; Beyond…</h2>
  <div class="rule" style="top:778px; width:376px;"></div>

  <p class="copy" style="top:796px;">Simply put, I help people who are local, relocating and investing, sell and purchase homes in Southern California. For purchases outside of California, I can refer to a network of agents across the country.</p>

  <p class="copy" style="top:896px;">I also provide a team who is dedicated to providing outstanding customer service throughout the transaction. My team includes a network of lenders, title, and escrow officers, in house CPA, stagers, photographers, contractors and more.</p>
</div>
</body>
</html>
```